Reed & Vale NC grand opening (for BILLBOARD)

Advertising the grand opening of our cannabis/hemp shop in NC. We will sell all things hemp (flower, cartridges, disposables, edibles, creams, lotions, pet products etc...)

Requirements
Must have
• include, open starting Aug 1, but grand opening Aug 15th.
Nice to have
• Difference slogan ideas "Save some cash, buy our grass" "Find your perfect high at Reed & Vale cannabis store" "Experience Nature's Gift: Reed & Vale Cannabis Store"

```html
<!DOCTYPE html>
<html lang="en">
<head>
<meta charset="UTF-8">
<title>Reed &amp; Vale – Grand Opening Billboard</title>
<link href="https://fonts.googleapis.com/css2?family=Poppins:wght@400;500;600;700;800&family=Great+Vibes&display=swap" rel="stylesheet">
<style>
  :root {
    --leaf-green: #78c54a;
    --deep-green: #1f6b3a;
    --navy: #161b38;
    --ink: #17192b;
    --wash-light: #f6faf2;
    --wash-mid: #e3f0d6;
    --white: #ffffff;
  }
  * { margin: 0; padding: 0; box-sizing: border-box; }
  html, body {
    width: 1200px; height: 442px; overflow: hidden;
    background: var(--white);
  }
  .billboard {
    position: relative; width: 1200px; height: 442px; overflow: hidden;
    font-family: "Poppins", sans-serif; color: var(--ink);
  }
  .floral-wash {
    position: absolute; inset: 0;
    background:
      radial-gradient(ellipse 420px 260px at 620px 230px, var(--wash-light) 0%, rgba(246,250,242,0) 100%),
      linear-gradient(90deg, var(--wash-mid) 0%, var(--wash-light) 45%, var(--wash-light) 60%, var(--wash-mid) 100%);
  }
  .waves { position: absolute; inset: 0; width: 1200px; height: 442px; }
  .brand-name {
    position: absolute; left: 0; width: 1236px; top: 78px;
    text-align: center;
    font-weight: 600; font-size: 70px; line-height: 1;
    color: var(--leaf-green); letter-spacing: -1px;
  }
  .tagline {
    position: absolute; right: 606px; top: 186px;
    text-align: right; font-size: 29px; line-height: 1.2;
    font-weight: 400;
  }
  .tagline .line { display: block; margin-bottom: 10px; }
  .tagline .highlight { color: var(--leaf-green); font-weight: 700; }
  .tagline .date { font-weight: 800; color: var(--leaf-green); }
  .tagline sup { font-size: 0.55em; vertical-align: 0.7em; }
  .divider {
    position: absolute; left: 621px; top: 190px;
    width: 2px; height: 152px; background: var(--navy);
  }
  .event-title {
    position: absolute; left: 652px; top: 186px; width: 230px;
  }
  .event-title .grand {
    position: relative; display: block;
    font-weight: 800; font-size: 66px; line-height: 1;
    color: var(--leaf-green); letter-spacing: -1px;
  }
  .event-title .opening {
    position: relative; display: block; font-family: "Great Vibes", cursive;
    font-size: 80px; line-height: 1; color: var(--deep-green);
    margin-top: -12px; margin-left: -8px;
  }
  .event-date {
    position: absolute; left: 896px; top: 193px;
    font-weight: 800; color: var(--navy); line-height: 1;
  }
  .event-date .day { display: block; font-size: 62px; letter-spacing: -2px; }
  .event-date .day sup { font-size: 27px; vertical-align: 25px; letter-spacing: 0; }
  .event-date .month { display: block; font-size: 64px; margin-top: 6px; letter-spacing: 1px; }
  .location-pill {
    position: absolute; left: 498px; top: 372px;
    width: 206px; height: 35px; border-radius: 18px;
    background: var(--navy); color: var(--white);
    font-size: 13.5px; font-weight: 500;
    display: flex; align-items: center; justify-content: center;
  }
</style>
</head>
<body>
<main class="billboard">
  <div class="floral-wash" role="img" aria-label="Soft pale green watercolour wash with line-drawn poppy flowers and leaves"></div>

  <svg class="waves" viewBox="0 0 1200 442" preserveAspectRatio="none" aria-hidden="true">
    <path fill="var(--leaf-green)" d="M0,0 H300 C262,36 232,62 205,112 C175,162 125,188 62,186 C32,185 12,180 0,175 Z"/>
    <path fill="var(--navy)" d="M68,0 H413 C392,30 362,50 322,49 C282,48 262,26 222,20 C182,14 142,30 102,20 C86,15 76,8 68,0 Z"/>
    <path fill="var(--navy)" d="M790,442 C822,410 852,394 892,394 C942,394 972,420 1022,418 C1072,416 1102,400 1136,410 L1136,442 Z"/>
    <path fill="var(--leaf-green)" d="M922,442 C962,402 1002,402 1042,382 C1082,362 1082,292 1132,272 C1162,260 1186,264 1200,272 V442 Z"/>
  </svg>

  <h1 class="brand-name">Reed &amp; Vale</h1>

  <p class="tagline">
    <span class="line">Find your perfect high at</span>
    <span class="line"><span class="highlight">Reed &amp; Vale cannabis</span> store</span>
    <span class="line">Open starting <span class="date">1<sup>st</sup> Aug</span></span>
  </p>

  <div class="divider"></div>

  <h2 class="event-title">
    <span class="grand">Grand</span>
    <span class="opening">Opening</span>
  </h2>

  <p class="event-date">
    <span class="day">15<sup>TH</sup></span>
    <span class="month">AUG</span>
  </p>

  <p class="location-pill">Exit 4B Maple Ridge Rd</p>
</main>
</body>
</html>
```